Business Card Design Project

Looking for a simple and stylish business card. We are an Advertising Company. The card Must feature the company logo (attached) and also this info.
p: 0461528390
e: sales@jh-promo.com.au
w: www.jh-promo.com.au
We Advertise mainly using TV screens featured in restaurants and cafe. See website for more about the business.
Not really looking for a plain background, but at the same time do not want to much happening in the Background. I am not really to fussy though with the design or the colour scheme, and I am leaving the creativity part up to you creative designers.
Business

```html
<!DOCTYPE html>
<html lang="en">
<head>
<meta charset="utf-8">
<title>JH Promo Business Card</title>
<link href="https://fonts.googleapis.com/css2?family=Questrial&family=Montserrat:wght@600&display=swap" rel="stylesheet">
<style>
  :root {
    --backdrop: #d9d9d9;
    --card: #1f1f1f;
    --card-light: #2a2a2a;
    --ink-white: #f2f2f2;
    --ink-soft: #cfcfcf;
    --brand-blue: #1f4fa6;
    --brand-pink: #e3245e;
    --tag-white: #ffffff;
  }
  * { margin: 0; padding: 0; box-sizing: border-box; }
  html, body { width: 1200px; height: 1000px; overflow: hidden; }
  body {
    background: var(--backdrop);
    font-family: "Questrial", "Century Gothic", sans-serif;
    position: relative;
  }
  .card {
    position: absolute;
    left: 240px;
    width: 720px;
    height: 410px;
    background: linear-gradient(135deg, var(--card-light), var(--card) 55%, #1a1a1a);
    box-shadow: 0 6px 18px rgba(0,0,0,0.25);
    color: var(--ink-white);
  }
  .card--front { top: 70px; }
  .card--back { top: 520px; }

  .front__tagline {
    position: absolute; right: 44px; top: 52px;
    font-family: "Montserrat", sans-serif; font-weight: 600;
    font-size: 21px; color: var(--ink-white);
  }
  .contact-line {
    position: absolute; right: 30px;
    display: flex; align-items: center; gap: 12px;
    font-size: 20px; color: var(--ink-soft); letter-spacing: 0.3px;
  }
  .contact-line::after {
    content: ""; display: block; width: 11px; height: 15px; background: var(--ink-white);
  }
  .contact-line--phone { top: 92px; }
  .contact-line--email { top: 250px; }
  .contact-line--web { top: 285px; }

  .brand-name {
    font-family: "Questrial", "Century Gothic", sans-serif;
    color: var(--brand-blue);
    letter-spacing: 1px;
    white-space: nowrap;
  }
  .front__brand {
    position: absolute; left: 40px; top: 150px;
    font-size: 64px; line-height: 1;
  }
  .name-tag {
    position: absolute; left: 375px; right: 0; top: 145px; height: 74px;
    background: var(--tag-white);
    border-radius: 14px 0 0 14px;
    display: flex; align-items: center; justify-content: space-between;
    padding: 0 22px 0 18px;
  }
  .name-tag__name {
    font-size: 38px; color: var(--brand-blue); letter-spacing: 0.5px;
  }
  .name-tag__bar {
    width: 16px; height: 54px; background: var(--brand-pink);
  }

  .back__brand {
    position: absolute; left: 0; right: 0; top: 120px;
    text-align: center; font-size: 104px; line-height: 1;
  }
  .back__web {
    position: absolute; left: 0; right: 0; top: 250px;
    text-align: center; font-size: 21px; color: var(--ink-white); letter-spacing: 0.3px;
  }
</style>
</head>
<body>
  <section class="card card--front">
    <p class="front__tagline">Advertising Company</p>
    <p class="contact-line contact-line--phone">phone | 0461528390</p>
    <p class="brand-name front__brand">JH PROMO</p>
    <div class="name-tag">
      <span class="name-tag__name">DANA WHITLEY</span>
      <span class="name-tag__bar"></span>
    </div>
    <p class="contact-line contact-line--email">email | sales@jh-promo.com.au</p>
    <p class="contact-line contact-line--web">www.jh-promo.com.au</p>
  </section>

  <section class="card card--back">
    <p class="brand-name back__brand">JH PROMO</p>
    <p class="back__web">www.jh-promo.com.au</p>
  </section>
</body>
</html>
```